Vacation giveaway landing page design

We are giving away a holiday/vacation to Rome and we need a landing page designed that will entice people to enter their email address for a chance to win!

Full brief, examples and everything else can be found in this document: https://files.quorvanshare.net/page/7-tmzrwpQY4vxkaLn8sbgeXu2fcTo5kWdn3jhpyuBc29m/open?mode=viewing

Number of Pages Required

1 page

```html
<!DOCTYPE html>
<html lang="en">
<head>
<meta charset="utf-8">
<title>The Voyage Club – Win a Trip to Rome</title>
<link href="https://fonts.googleapis.com/css2?family=Montserrat:wght@400;600;700;800&family=Open+Sans:wght@400;600;700&display=swap" rel="stylesheet">
<style>
:root{
  --red:#f0554f;
  --teal:#1c8aa3;
  --teal-light:#5fcfd0;
  --label-teal:#1fa1b3;
  --navy:#1b5f7c;
  --blue:#0ca1e6;
  --ink:#2b2b2b;
  --muted:#777;
  --line:#dfe6ea;
  --white:#fff;
  --black:#0b0b0b;
  --gold:#f2c231;
  --head:"Montserrat",sans-serif;
  --body:"Open Sans",sans-serif;
}
*{box-sizing:border-box;margin:0;padding:0}
html,body{width:1200px;height:4639px;overflow:hidden}
body{position:relative;font-family:var(--body);color:var(--ink);background:var(--white)}
.section{position:absolute;left:0;width:1200px}
.abs{position:absolute}
.ph{position:absolute}

/* Nav */
.brand{position:absolute;display:flex;align-items:center;gap:12px;font-family:var(--head);font-weight:700;color:var(--white);letter-spacing:1px}
.brand-dot{width:34px;height:34px;border-radius:50%;border:3px solid var(--white)}
.nav{position:absolute;top:52px;right:78px;display:flex;gap:42px;font-family:var(--body);font-size:15px;color:var(--white)}

/* Hero */
.hero{top:0;height:665px;overflow:hidden}
.hero-photo{left:0;top:0;width:1200px;height:665px;background:linear-gradient(180deg,#f7a04c 0%,#f4b066 28%,#c98e6d 55%,#8d7c78 80%,#6f6a6d 100%)}
.hero-panel{left:0;top:0;width:330px;height:665px;background:var(--red)}
.hero-title{position:absolute;left:77px;top:180px;width:560px;font-family:var(--head);font-weight:800;font-size:31px;line-height:40px;color:var(--white);text-transform:uppercase}
.signup{position:absolute;left:77px;top:282px;width:510px;height:40px;display:flex}
.signup input{flex:1;border:0;padding:0 16px;font-family:var(--body);font-size:13px;color:#555}
.signup button{width:130px;border:0;background:var(--teal);color:var(--white);font-family:var(--body);font-weight:700;font-size:14px}
.hero-person{left:60px;top:360px;width:240px;height:300px;border-radius:8px;background:linear-gradient(180deg,#e9c9b0,#c8322d 45%,#2f3b66);opacity:.9}
.hero-group{left:700px;top:250px;width:460px;height:415px;border-radius:8px;background:linear-gradient(180deg,#c9a27f,#4f7eb3 45%,#42465c);opacity:.6}

/* Section title */
.sec-title{position:absolute;left:0;width:1200px;text-align:center;font-family:var(--head);font-weight:700;font-size:31px;letter-spacing:1px;color:var(--navy)}
.sec-title .accent{color:var(--red)}
.title-mark{position:absolute;left:590px;width:20px;height:20px;border-radius:50%;border:2px solid var(--red)}

/* Winners */
.winners{top:665px;height:705px}
.win-card{position:absolute;top:155px;width:322px;height:500px;background:var(--white);box-shadow:0 4px 18px rgba(0,0,0,.12)}
.win-photo{position:absolute;left:0;top:0;width:322px;height:290px}
.win-tag{position:absolute;left:12px;top:10px;color:var(--white);font-family:var(--body);font-size:12px;line-height:15px}
.win-tag b{display:block;font-weight:700}
.win-social{position:absolute;right:12px;top:10px;width:22px;height:22px;background:var(--white);border-radius:3px}
.win-label{position:absolute;left:0;top:230px;width:322px;height:60px;background:var(--label-teal);color:var(--white);font-family:var(--head);font-weight:700;font-size:14px;line-height:19px;padding:12px 14px;text-transform:uppercase}
.win-label span{color:#fbe36a}
.win-text{position:absolute;left:14px;top:310px;width:250px;font-size:13px;line-height:22px;color:#444}
.win-text a{color:var(--red);text-decoration:none}
.win-icons{position:absolute;right:14px;top:310px;display:flex;flex-direction:column;gap:14px}
.slide-arrow{position:absolute;top:352px;width:30px;height:30px;border-radius:50%;background:#fff;border:2px solid #333;display:flex;align-items:center;justify-content:center}

/* Countdown */
.countdown{top:1370px;height:538px}
.count-bg{left:0;top:0;width:1200px;height:538px;background:linear-gradient(180deg,#3f3a37 0%,#5c524b 45%,#6b5b4c 70%,#3d3631 100%)}
.count-title{position:absolute;top:68px;left:0;width:1200px;text-align:center;font-family:var(--head);font-weight:700;font-size:31px;color:var(--white);letter-spacing:1px}
.unit{position:absolute;top:180px;width:100px;text-align:center;color:var(--white)}
.unit-label{font-family:var(--head);font-weight:700;font-size:13px;letter-spacing:1px}
.unit-ring{margin:18px auto 0;width:86px;height:86px;border-radius:50%;border:4px solid var(--gold);background:rgba(0,0,0,.35);display:flex;align-items:center;justify-content:center;font-family:var(--head);font-weight:700;font-size:30px}
.colon{position:absolute;top:222px;font-family:var(--head);font-weight:700;font-size:34px;color:var(--white)}
.unit-hang{margin:14px auto 0;width:70px;height:56px;border-radius:6px;background:linear-gradient(180deg,#f0c64a,#4fb8a8);opacity:.7}
.join-title{position:absolute;top:418px;left:0;width:1200px;text-align:center;font-family:var(--head);font-weight:800;font-size:31px;color:var(--white)}

/* Pricing */
.pricing{top:1908px;height:551px}
.price-person{left:30px;top:95px;width:350px;height:380px;border-radius:10px;background:linear-gradient(180deg,#d7b988,#e2823b 40%,#3f7d3a 70%,#2f4f27)}
.plan{position:absolute;background:var(--white);box-shadow:0 6px 24px rgba(0,0,0,.14);text-align:center}
.plan-head{height:46px;display:flex;align-items:center;justify-content:center;font-family:var(--head);font-weight:700;font-size:14px;color:var(--white);text-transform:uppercase}
.plan-price{font-family:var(--head);font-weight:700;color:var(--navy);margin-top:26px}
.plan-sub{font-size:12px;color:var(--muted);margin-top:4px}
.plan-list{list-style:none;text-align:left;margin:22px 0 0 28px;font-size:12px;line-height:26px;color:#444}
.plan-list li::before{content:"✓";color:var(--teal);font-weight:700;margin-right:8px}
.plan-btn{display:block;margin:22px auto 0;height:38px;line-height:38px;color:var(--white);font-size:13px;font-weight:600}
.plan-cancel{font-size:12px;color:#555;margin-top:12px}

/* Prize */
.prize{top:2459px;height:479px;overflow:hidden}
.prize-bg{left:0;top:0;width:1200px;height:479px;background:linear-gradient(180deg,#2d3c4a 0%,#7d8b95 35%,#c9ced2 55%,#6a7077 80%,#2c3036 100%)}
.prize-title{position:absolute;left:77px;top:86px;font-family:var(--head);font-weight:800;font-size:38px;color:var(--white)}
.prize-list{position:absolute;left:77px;top:150px;font-family:var(--body);font-size:23px;line-height:44px;color:var(--white)}
.stars{position:absolute;left:77px;top:292px;display:flex;gap:8px}
.btn-teal{position:absolute;background:var(--teal);color:var(--white);font-size:14px;font-weight:600;text-align:center}

/* FAQ */
.faq{top:2938px;height:560px}
.faq-item{position:absolute;width:400px;min-height:46px;border:1px solid var(--line);background:var(--white);font-size:13px;line-height:18px;padding:14px 40px 12px 16px;color:#333}
.faq-item .chev{position:absolute;right:14px;top:16px}
.faq-item.open{background:var(--teal);color:var(--white);border-color:var(--teal)}
.faq-item.open p{font-size:11px;line-height:16px;margin-top:6px;opacity:.9}
.faq-visual{left:482px;top:207px;width:236px;height:236px;border-radius:50%;background:radial-gradient(circle,#dcdad6 0%,#eeeeec 55%,rgba(255,255,255,0) 72%)}

/* Magazine */
.magazine{top:3430px;height:1209px}
.mag-title{position:absolute;top:322px;left:0;width:1200px;text-align:center;font-family:var(--head);font-weight:700;font-size:31px;color:var(--white);letter-spacing:1px}
.mag-cover{left:170px;top:420px;width:420px;height:290px;border-radius:6px;background:linear-gradient(135deg,#e9edf0,#35414c 45%,#6a8a5f 75%,#dfe3e6)}
.mag-feat{position:absolute;left:640px;top:468px;display:grid;grid-template-columns:180px 240px;row-gap:20px;font-family:var(--head);font-weight:600;font-size:15px;color:var(--white);white-space:nowrap}
.mag-feat span{display:flex;align-items:center;gap:10px}
.mag-feat i{width:14px;height:14px;border-radius:50%;border:2px solid var(--white);display:inline-block}
.mag-person{left:860px;top:640px;width:300px;height:440px;border-radius:10px;background:linear-gradient(180deg,#e1c08b,#d9a57c 25%,#4a9ac9 50%,#2b2f45)}

/* Footer */
.foot-brand{left:0;width:1200px;justify-content:center}
.contacts{position:absolute;top:990px;left:0;width:1200px;display:flex;justify-content:center;gap:40px;font-size:13px;color:#ddd}
.contacts span{display:flex;align-items:center;gap:8px}
.address{position:absolute;top:1020px;left:0;width:1200px;text-align:center;font-size:13px;line-height:20px;color:#ccc}
.social{position:absolute;top:1076px;left:0;width:1200px;display:flex;justify-content:center;gap:18px}
.social i{width:18px;height:18px;border-radius:50%;background:#cfcfcf;display:block}
.foot-bar{position:absolute;top:1126px;left:0;width:1200px;height:83px;border-top:1px solid #333}
.copy{position:absolute;left:160px;top:30px;font-size:12px;color:#bbb}
.copy b{color:var(--red);font-weight:600}
.foot-nav{position:absolute;right:130px;top:28px;display:flex;gap:44px;font-size:14px;color:#ddd}
.foot-nav .on{color:var(--red)}
</style>
</head>
<body>

<!-- HERO -->
<section class="section hero">
  <div class="ph hero-photo" role="img" aria-label="Photo of the Colosseum in Rome at sunset with a car, a plane and travellers with suitcases"></div>
  <div class="ph hero-panel"></div>
  <div class="ph hero-person" role="img" aria-label="Photo of a smiling woman in a red jacket sitting on the ground"></div>
  <div class="ph hero-group" role="img" aria-label="Photo of a group of tourists with luggage"></div>
  <div class="brand" style="left:77px;top:38px;font-size:18px"><span class="brand-dot"></span>THE VOYAGE CLUB</div>
  <nav class="nav"><span>Home</span><span>Hotels</span><span>Flight</span><span>Tour</span><span>Contact us</span></nav>
  <h1 class="hero-title">Enter your email id to win a prize to Rome!</h1>
  <form class="signup"><input type="text" value="Enter Your Email ..."><button type="button">Subscribe</button></form>
</section>

<!-- PREVIOUS WINNERS -->
<section class="section winners">
  <h2 class="sec-title" style="top:48px">PREVIOUS <span class="accent">WINNERS</span></h2>
  <span class="title-mark" style="top:96px"></span>

  <div class="slide-arrow" style="left:30px"><svg width="10" height="12"><path d="M8 1L2 6l6 5" fill="none" stroke="#333" stroke-width="2"/></svg></div>
  <div class="slide-arrow" style="left:1140px"><svg width="10" height="12"><path d="M2 1l6 5-6 5" fill="none" stroke="#333" stroke-width="2"/></svg></div>

  <article class="win-card" style="left:84px">
    <div class="win-photo" role="img" aria-label="Portrait photo of April's prize winner" style="background:linear-gradient(160deg,#8a6a58,#c99a86 50%,#4a3a36)"></div>
    <div class="win-tag"><b>The Voyage Club</b>about 8 months ago</div><span class="win-social"></span>
    <div class="win-label">April's winner prize:<br><span>A week in Portugal</span></div>
    <p class="win-text">Congratulations to this month's winner — she has won a week long holiday in sunny Portugal!<br>Next month you could win 7 nights in the Canary Islands. Sign up here –<br><a>vyg.example/a1</a></p>
    <div class="win-icons"><svg width="16" height="14"><path d="M2 6h3v7H2zM5 6l4-5 1 1-1 4h5l-1 7H5" fill="none" stroke="#888" stroke-width="1.3"/></svg><svg width="16" height="14"><path d="M1 2h14v8H6l-4 3V10H1z" fill="none" stroke="#888" stroke-width="1.3"/></svg><svg width="16" height="14"><path d="M1 13c2-6 6-8 10-8V2l4 5-4 5V9c-4 0-7 1-10 4z" fill="none" stroke="#888" stroke-width="1.3"/></svg></div>
  </article>

  <article class="win-card" style="left:436px">
    <div class="win-photo" role="img" aria-label="Photo of October's prize winner in a city street" style="background:linear-gradient(160deg,#6f7a80,#a99080 50%,#3a3431)"></div>
    <div class="win-tag"><b>The Voyage Club</b>about 8 months ago</div><span class="win-social"></span>
    <div class="win-label">October's winner prize:<br><span>A week in the Canary Islands</span></div>
    <p class="win-text">This month's winner, Lena Hartwell, is escaping to the Canary Islands for a week long getaway!<br>Next month's giveaway: 7 nights on the beautiful coast of Portugal. Enter now<br><a>vyg.example/b2</a></p>
    <div class="win-icons"><svg width="16" height="14"><path d="M2 6h3v7H2zM5 6l4-5 1 1-1 4h5l-1 7H5" fill="none" stroke="#888" stroke-width="1.3"/></svg><svg width="16" height="14"><path d="M1 2h14v8H6l-4 3V10H1z" fill="none" stroke="#888" stroke-width="1.3"/></svg><svg width="16" height="14"><path d="M1 13c2-6 6-8 10-8V2l4 5-4 5V9c-4 0-7 1-10 4z" fill="none" stroke="#888" stroke-width="1.3"/></svg></div>
  </article>

  <article class="win-card" style="left:798px">
    <div class="win-photo" role="img" aria-label="Photo of February's prize winner outdoors" style="background:linear-gradient(160deg,#a8a090,#c8b09a 50%,#5a5048)"></div>
    <div class="win-tag"><b>The Voyage Club</b>about 8 months ago</div><span class="win-social"></span>
    <div class="win-label">February's winner prize:<br><span>Flights to New York City</span></div>
    <p class="win-text">New York, New York! Congratulations to Marcus Bell — he's won flights for two to the Big Apple.<br>Next month's prize? A week long holiday in the Greek Islands! Enter here –<br><a>vyg.example/c3</a></p>
    <div class="win-icons"><svg width="16" height="14"><path d="M2 6h3v7H2zM5 6l4-5 1 1-1 4h5l-1 7H5" fill="none" stroke="#888" stroke-width="1.3"/></svg><svg width="16" height="14"><path d="M1 2h14v8H6l-4 3V10H1z" fill="none" stroke="#888" stroke-width="1.3"/></svg><svg width="16" height="14"><path d="M1 13c2-6 6-8 10-8V2l4 5-4 5V9c-4 0-7 1-10 4z" fill="none" stroke="#888" stroke-width="1.3"/></svg></div>
  </article>
</section>

<!-- COUNTDOWN -->
<section class="section countdown">
  <div class="ph count-bg" role="img" aria-label="Photo of Rome at dusk with St Peter's dome and a river bridge"></div>
  <h2 class="count-title">PRIZE DRAW CLOSES IN</h2>
  <span class="title-mark" style="top:116px;border-color:#fff"></span>

  <div class="unit" style="left:150px"><div class="unit-label">DAYS</div><div class="unit-ring">04</div><div class="unit-hang" role="img" aria-label="Dreamcatcher decoration"></div></div>
  <div class="colon" style="left:330px">:</div>
  <div class="unit" style="left:410px"><div class="unit-label">HOURS</div><div class="unit-ring">12</div><div class="unit-hang" role="img" aria-label="Dreamcatcher decoration"></div></div>
  <div class="colon" style="left:600px">:</div>
  <div class="unit" style="left:690px"><div class="unit-label">MIN</div><div class="unit-ring">18</div><div class="unit-hang" role="img" aria-label="Dreamcatcher decoration"></div></div>
  <div class="colon" style="left:870px">:</div>
  <div class="unit" style="left:955px"><div class="unit-label">SEC</div><div class="unit-ring">08</div><div class="unit-hang" role="img" aria-label="Dreamcatcher decoration"></div></div>

  <h2 class="join-title">JOIN NOW!</h2>
  <svg class="abs" style="left:555px;top:498px" width="90" height="40"><path d="M0 40L45 0l45 40z" fill="#fff"/></svg>
</section>

<!-- PRICING -->
<section class="section pricing">
  <div class="ph price-person" role="img" aria-label="Photo of a cheerful traveller in a straw hat with a stack of suitcases"></div>

  <div class="plan" style="left:467px;top:96px;width:322px;height:378px">
    <div class="plan-head" style="background:var(--red)">15 Entries &amp; Weekly Deals</div>
    <div class="plan-price" style="font-size:34px">£4.99</div>
    <div class="plan-sub">Per Month / Was £6.00</div>
    <ul class="plan-list">
      <li>Weekly Deals Email</li><li>Save £100's on Holidays</li><li>Monthly Magazine</li><li>15 Entries Every Month</li>
    </ul>
    <span class="plan-btn" style="width:200px;background:var(--red)">Go To Checkout</span>
    <div class="plan-cancel">Cancel Anytime</div>
  </div>

  <div class="plan" style="left:866px;top:133px;width:254px;height:310px">
    <div class="plan-head" style="background:var(--teal-light);height:40px;font-size:12px">1 Entry</div>
    <div class="plan-price" style="font-size:30px;margin-top:20px">£2.99</div>
    <div class="plan-sub">Per Month</div>
    <ul class="plan-list" style="margin:16px 0 0 22px;line-height:22px;font-size:11px">
      <li>Weekly Deals Email</li><li>Save £100's on Holidays</li><li>Monthly Magazine</li><li>1 Entries Every Month</li>
    </ul>
    <span class="plan-btn" style="width:160px;height:32px;line-height:32px;margin-top:16px;font-size:12px;background:var(--teal-light)">Go To Checkout</span>
    <div class="plan-cancel" style="font-size:11px;margin-top:8px">Cancel Anytime</div>
  </div>
</section>

<!-- THIS MONTH'S PRIZE -->
<section class="section prize">
  <div class="ph prize-bg" role="img" aria-label="Photo of a cliff-top viewing platform above misty clouds with a plane flying"></div>
  <h2 class="prize-title">THIS MONTH'S PRIZE</h2>
  <div class="prize-list">4 Nights, 2 people<br>Rome<br>Flights + Hotel</div>
  <div class="stars">
    <svg width="22" height="22" viewBox="0 0 24 24"><path d="M12 1l3.2 7 7.6.8-5.7 5.1 1.6 7.5L12 17.6 5.3 21.4l1.6-7.5L1.2 8.8 8.8 8z" fill="var(--gold)"/></svg>
    <svg width="22" height="22" viewBox="0 0 24 24"><path d="M12 1l3.2 7 7.6.8-5.7 5.1 1.6 7.5L12 17.6 5.3 21.4l1.6-7.5L1.2 8.8 8.8 8z" fill="var(--gold)"/></svg>
    <svg width="22" height="22" viewBox="0 0 24 24"><path d="M12 1l3.2 7 7.6.8-5.7 5.1 1.6 7.5L12 17.6 5.3 21.4l1.6-7.5L1.2 8.8 8.8 8z" fill="var(--gold)"/></svg>
    <svg width="22" height="22" viewBox="0 0 24 24"><path d="M12 1l3.2 7 7.6.8-5.7 5.1 1.6 7.5L12 17.6 5.3 21.4l1.6-7.5L1.2 8.8 8.8 8z" fill="var(--gold)"/></svg>
    <svg width="22" height="22" viewBox="0 0 24 24"><path d="M12 1l3.2 7 7.6.8-5.7 5.1 1.6 7.5L12 17.6 5.3 21.4l1.6-7.5L1.2 8.8 8.8 8z" fill="var(--gold)"/></svg>
  </div>
  <span class="btn-teal" style="left:77px;top:362px;width:118px;height:40px;line-height:40px">Join Now</span>
</section>

<!-- FAQ -->
<section class="section faq">
  <h2 class="sec-title" style="top:84px;color:var(--red)">FAQ</h2>
  <span class="title-mark" style="top:130px"></span>

  <div class="ph faq-visual" role="img" aria-label="Illustration of an antique key surrounded by soft rings"></div>

  <div class="faq-item" style="left:84px;top:210px">Can I enter just this month's prize draw?<svg class="chev" width="14" height="8"><path d="M1 1l6 6 6-6" fill="none" stroke="#5fb7c9" stroke-width="2"/></svg></div>
  <div class="faq-item open" style="left:84px;top:276px;height:74px">What are my odds of actually winning?<p>It varies each month, but right now the odds are really good because entries are still low!</p><svg class="chev" width="14" height="8"><path d="M1 1l6 6 6-6" fill="none" stroke="#fff" stroke-width="2"/></svg></div>
  <div class="faq-item" style="left:84px;top:366px">When are the winners announced &amp; how will I know if I've won?<svg class="chev" width="14" height="8"><path d="M1 1l6 6 6-6" fill="none" stroke="#5fb7c9" stroke-width="2"/></svg></div>
  <div class="faq-item" style="left:84px;top:440px">Do you sell or share any of my details?<svg class="chev" width="14" height="8"><path d="M1 1l6 6 6-6" fill="none" stroke="#5fb7c9" stroke-width="2"/></svg></div>

  <div class="faq-item" style="left:720px;top:210px">What do runners up get?<svg class="chev" width="14" height="8"><path d="M1 1l6 6 6-6" fill="none" stroke="#5fb7c9" stroke-width="2"/></svg></div>
  <div class="faq-item" style="left:720px;top:276px">How are the winners decided?<svg class="chev" width="14" height="8"><path d="M1 1l6 6 6-6" fill="none" stroke="#5fb7c9" stroke-width="2"/></svg></div>
  <div class="faq-item" style="left:720px;top:342px">Who are you?<svg class="chev" width="14" height="8"><path d="M1 1l6 6 6-6" fill="none" stroke="#5fb7c9" stroke-width="2"/></svg></div>
  <div class="faq-item" style="left:720px;top:408px">I've got a question not listed here!<svg class="chev" width="14" height="8"><path d="M1 1l6 6 6-6" fill="none" stroke="#5fb7c9" stroke-width="2"/></svg></div>
</section>

<!-- MAGAZINE + FOOTER -->
<section class="section magazine">
  <svg class="abs" style="left:0;top:0" width="1200" height="1209" viewBox="0 0 1200 1209">
    <path d="M0 120 C120 40 220 30 330 80 C430 125 520 60 640 40 C760 20 830 110 930 90 C1030 70 1100 10 1200 30 L1200 1209 L0 1209Z" fill="var(--blue)"/>
    <path d="M0 140 C140 70 240 70 340 110 C450 150 540 90 660 70 C780 55 850 130 950 115 C1050 100 1120 50 1200 60" fill="none" stroke="#5cc6f2" stroke-width="6" opacity=".5"/>
    <path d="M0 740 C150 680 280 700 400 750 C520 800 640 760 760 700 C880 640 1000 700 1200 650 L1200 1209 L0 1209Z" fill="var(--black)"/>
  </svg>

  <h2 class="mag-title">MONTHLY MAGAZINE</h2>
  <span class="title-mark" style="top:368px;border-color:#fff"></span>
  <div class="ph mag-cover" role="img" aria-label="Fanned stack of travel magazine covers with mountain and city photos"></div>
  <div class="mag-feat">
    <span><i></i>INTERVIEWS</span><span><i></i>CITY GUIDES</span>
    <span><i></i>DISCOUNTS</span><span><i></i>CHEAP FLIGHT ALERTS</span>
  </div>
  <span class="btn-teal" style="left:640px;top:568px;width:160px;height:40px;line-height:40px;background:var(--teal)">Join Now</span>
  <div class="ph mag-person" role="img" aria-label="Photo of a smiling traveller in a hat holding a passport with a camera"></div>

  <div class="brand foot-brand" style="top:880px;font-size:22px"><span class="brand-dot" style="width:40px;height:40px"></span>THE VOYAGE CLUB</div>
  <div class="contacts">
    <span><svg width="14" height="14" viewBox="0 0 24 24"><path d="M6.6 10.8a15 15 0 006.6 6.6l2.2-2.2a1 1 0 011-.25 11.4 11.4 0 003.6.57 1 1 0 011 1V20a1 1 0 01-1 1A17 17 0 013 4a1 1 0 011-1h3.5a1 1 0 011 1 11.4 11.4 0 00.57 3.6 1 1 0 01-.25 1z" fill="var(--red)"/></svg>(0100) 555 0148</span>
    <span><svg width="14" height="12" viewBox="0 0 24 20"><rect x="1" y="1" width="22" height="18" rx="2" fill="none" stroke="var(--red)" stroke-width="2"/><path d="M1 2l11 9 11-9" fill="none" stroke="var(--red)" stroke-width="2"/></svg>hello@voyageclub.example</span>
  </div>
  <div class="address">12 Harbour Lane, Suite 4<br>Brightwater</div>
  <div class="social"><i></i><i></i><i></i><i></i></div>
  <div class="foot-bar">
    <div class="copy">Copyright © 2018 <b>THE VOYAGE CLUB</b> | All Rights Reserved</div>
    <nav class="foot-nav"><span class="on">Home</span><span>Hotels</span><span>Flight</span><span>Tour</span><span>Contact us</span></nav>
  </div>
</section>

</body>
</html>
```